Web Design Home Page

KRVL Athletics.com – Homepage Vision
KRVL is a community based youth sports program currently running basketball and soccer programs. We run recreational leagues, competitive club programs and run many camps, clinics and development programs in both sports.
My vision on the KRVL Home page was to design a clean page that will guide viewers quickly to the sport of interest.
At the top I was thinking of a KRVL Logo Bar. I want something that we can also customize for each of the sports to use in the future. So, 5 different logo bars.
1 – KRVL Athletics Logo Bar – Goes on the KRVLAthletics.com home page, which give general information about the club as a whole and leads folks to the sport they want to go.
2 – KRVL Basketball – Recreational. Same look as the homepage logo bar but only contains info regarding to recreational basketball.
3 – KRVL Basketball – Competitive. Same as above but only competitive basketball.
4 – KRVL Soccer – Recreational. Same as above but only recreational soccer.
5 – KRVL Soccer – Competitive. Same as above but only competitive soccer.
Maybe the logo bar on the home page can also be the main logo bar and also rotate the other 4 underneath the main logo bar. Logo are old, may need to be updated at some point.
The middle section, I was thinking of 4 boxes that when clicked on will take you to the appropriate website. The designs I used are just to show something. I took the picture off the web and they may be copyrighted so would probably need some type of original designs.
Recreational Basketball Website - http://krvlathletics-example.com/basketball/index.html
Competitive Basketball Website - http://www.krvlherons-example.com/
Recreational Soccer Website - http://krvlathletics-example.com/soccer/index.html
Competitive Soccer Website - http://www.ridgepremiersoccer-example.com/
Recreational basketball uses Granite Mesa Basketball (we own the trade name) or KRVL Basketball.
The competitive basketball club is known as KRVL Herons.
Recreational soccer goes by Granite Mesa Soccer or Granite Mesa Soccer Club.
Competitive soccer goes by Ridge Premier Soccer or Granite Mesa Soccer Club.
Then on the bottom of the page I was thinking of a menus bar that contains information general to the club (both basketball and soccer). When you click on any a pop up box will pop up with the information for each listed below.
About Us
Granite Mesa Athletic Club provides recreational leagues for both Basketball and Soccer with the focus placed on providing our youth with the rewarding opportunity of participating in youth sports. Our direction is to promote the recreational value of youth sports while emphasizing fun and respect for the sport.
Granite Mesa Athletic Club (KRVL) is based in the North Phoenix area with most of our players residing in the Willow Bend School District.
Our Mission
Our mission at Granite Mesa Athletic Club is to promote and develop excellence in youth sports based on skill, sportsmanship, values, and player character. Our programs aim to provide an environment for natural player development that prepares them for life experiences, both on and off the field.
We focus on a uniform sports philosophy throughout the club that emphasizes growth through positive reinforcement resulting in players achieving his/her fullest potential. We do not look for the next victory to measure our success, but in the total learning experience for each player, realizing that the team is much stronger than an individual.
Contact Info
Granite Mesa Athletic Club
P.O. Box 7068
Willow Bend, AZ 85990
Club Phone – 480-555-0173
Club Website – KRVLAthletics.com
Club Email – info@krvlathletics-example.com
Basketball Email – KRVLBB@mail-example.com
Soccer Email – KRVLSoccer@mail-example.com
Our Mission
The mission of KRVL shall be to promote good citizenship and health through community athletic activities for children and for educational purposes. Club focus is on player development, with emphasis on teamwork and sportsmanship with high standards for both parents and players. Respect, commitment and accountability are qualities we ask all our members to endorse both on and off the field.

```html
<!DOCTYPE html>
<html lang="en">
<head>
<meta charset="utf-8">
<title>Granite Mesa Athletic Club – Home</title>
<link rel="stylesheet" href="https://fonts.googleapis.com/css2?family=Cinzel:wght@400&family=PT+Sans:wght@400;700&family=PT+Sans+Narrow&display=swap">
<style>
:root{
  --page:#f2f2f2;
  --card:#faf8f9;
  --navy-top:#3d62aa;
  --navy-bottom:#22407f;
  --pill-top:#1f5e9a;
  --pill-bottom:#0a386a;
  --ink:#222;
  --accent:#1d3f78;
  --rule:#dddddd;
}
*{margin:0;padding:0;box-sizing:border-box}
html,body{width:1200px;height:1000px;overflow:hidden;background:var(--page)}
body{position:relative;font-family:Arial,Helvetica,sans-serif;color:var(--ink)}
.card{position:absolute;left:101px;top:28px;width:997px;height:895px;background:var(--card);border-radius:5px;overflow:hidden}
.banner{position:absolute;left:0;top:0;width:997px;height:105px;background:linear-gradient(var(--navy-top),var(--navy-bottom))}
.banner svg.corners{position:absolute;left:0;top:0}
.ball{position:absolute;width:54px;height:54px;border-radius:50%}
.ball--basket{left:26px;top:3px;background:radial-gradient(circle at 35% 30%,#e6e6e6,#7a7a7a 70%,#444)}
.ball--soccer{left:931px;top:5px;background:radial-gradient(circle at 35% 30%,#ffffff,#bcbcbc 70%,#555)}
.club-title{position:absolute;left:0;width:997px;top:30px;text-align:center;font-family:'Cinzel',serif;font-size:35px;color:#fff;letter-spacing:2px}
.tagline{position:absolute;left:0;width:997px;top:76px;text-align:center;font-size:15px;color:#fff;letter-spacing:.4px}
.tagline small{font-size:12.5px}
.program{position:absolute;top:148px;width:300px;text-align:center;font-family:'PT Sans',sans-serif;font-size:13.5px}
.program .sport{color:var(--accent)}
.program b{color:#000}
.program p{margin-bottom:7px}
.program p.sub{font-size:12.5px}
.program--basket{left:19px}
.program--soccer{left:680px}
.mark{display:flex;align-items:center;justify-content:center;gap:8px;margin-top:24px;font-family:'PT Sans',sans-serif;font-weight:700;font-size:17px;color:#111;line-height:1.1}
.mark .dot{width:22px;height:22px;border-radius:50%;background:#111;flex:none}
.club-mark{position:absolute;left:330px;top:130px;width:330px;height:230px;display:flex;align-items:center;justify-content:center;gap:14px;font-family:'PT Sans',sans-serif;font-weight:700;font-size:40px;color:var(--accent)}
.club-mark .dot{width:40px;height:40px;border-radius:50%;background:var(--accent);flex:none}
.camps{position:absolute;left:0;width:1020px;top:331px;text-align:center;font-family:'PT Sans',sans-serif;font-size:17px;color:#222}
.pill{position:absolute;top:373px;width:442px;height:37px;border-radius:18px;background:linear-gradient(var(--pill-top),var(--pill-bottom));color:#fff;text-align:center;font-family:'PT Sans',sans-serif;font-size:18px;letter-spacing:1.5px;line-height:37px}
.pill--who{left:16px}
.pill--mission{left:549px}
.copy{position:absolute;width:432px;font-size:12.6px;line-height:18px;letter-spacing:.6px;color:var(--ink)}
.copy p+p{margin-top:18px}
.copy--who{left:24px;top:418px}
.copy--mission{left:557px;top:429px}
.section-title{position:absolute;left:17px;top:612px;font-family:'PT Sans',sans-serif;font-size:18px;letter-spacing:1.5px;color:#1b4a7d}
.rule{position:absolute;left:23px;top:649px;width:937px;height:1px;background:var(--rule)}
.tile{position:absolute;top:678px;height:194px;display:block;text-decoration:none}
.tile .label{position:absolute;left:0;right:0;top:132px;height:34px;background:rgba(245,245,245,.85);display:flex;align-items:center;padding-left:8px;font-size:18px;color:#000}
.tile .label em{font-style:normal;color:var(--accent);margin-right:5px}
.tile .label svg{position:absolute;right:8px;top:7px}
.tile--rb{left:16px;width:230px;background:linear-gradient(135deg,#3a2a1e,#8a4a22 55%,#2a1a12)}
.tile--rs{left:257px;width:234px;background:linear-gradient(#2f7fd6,#9cc9ef 40%,#4c8a2a 62%,#2f6a1a)}
.tile--cb{left:506px;width:234px;background:linear-gradient(#f4f4f4,#dcd6d2 55%,#a85a42)}
.tile--cs{left:757px;width:229px;background:linear-gradient(#2f5a22,#4f8a32 55%,#2c5a1c)}
.footer-nav{position:absolute;left:0;width:1186px;top:950px;text-align:center;font-family:'PT Sans Narrow',sans-serif;font-size:12px;color:#000;word-spacing:1px}
.footer-nav a{color:#000;text-decoration:none}
.footer-nav span{margin:0 7px}
</style>
</head>
<body>
<main class="card">
  <header class="banner">
    <svg class="corners" width="997" height="105" viewBox="0 0 997 105" aria-hidden="true">
      <path d="M0 0 H126 C120 50 70 72 0 80 Z" fill="#f7f7f7"/>
      <path d="M997 0 H872 C876 50 930 82 997 86 Z" fill="#f7f7f7"/>
    </svg>
    <div class="ball ball--basket" role="img" aria-label="Basketball"></div>
    <div class="ball ball--soccer" role="img" aria-label="Soccer ball"></div>
    <h1 class="club-title">GRANITE MESA ATHLETIC CLUB</h1>
    <p class="tagline">Promoting good citizenship and health through <small>community athletic activities for children.</small></p>
  </header>

  <section class="program program--basket">
    <p><span class="sport">YOUTH BASKETBALL –</span> <b>GRADES K-12</b></p>
    <p class="sub">RECREATIONAL AND COMPETITIVE</p>
    <div class="mark"><span class="dot"></span>Granite Mesa<br>Basketball</div>
  </section>

  <div class="club-mark"><span class="dot"></span>KRVL</div>

  <section class="program program--soccer">
    <p><span class="sport">YOUTH SOCCER</span> <b>AGES 3-18</b></p>
    <p class="sub">RECREATIONAL AND COMPETITIVE</p>
    <div class="mark"><span class="dot"></span>Granite Mesa<br>Soccer Club</div>
  </section>

  <p class="camps">Both Sports Provide Many Camps Clinics and Developmental Programs</p>

  <h2 class="pill pill--who">WHO WE ARE?</h2>
  <div class="copy copy--who">
    <p>Granite Mesa Athletic Club provides recreational leagues for both Basketball and Soccer with the focus placed on providing our youth with the rewarding opportunity of participating in youth sports. Our direction is to promote the recreational value of youth sports while emphasizing fun and respect for the sport.</p>
    <p>Granite Mesa Athletic Club (KRVL) is based in the North Phoenix area with most of our players residing in the Willow Bend School District.</p>
  </div>

  <h2 class="pill pill--mission">OUR MISSION</h2>
  <div class="copy copy--mission">
    <p>The mission of KRVL shall be to promote good citizenship and health through community athletic activities for children and for educational purposes.</p>
    <p>Club focus is on player development, with emphasis on teamwork and sportsmanship with high standards for both parents and players. Respect, commitment and accountability are qualities we ask all our members to endorse both on and off it</p>
  </div>

  <h2 class="section-title">OUR SPORTS</h2>
  <div class="rule"></div>

  <a class="tile tile--rb" href="http://krvlathletics-example.com/basketball/index.html" role="img" aria-label="Photo of a basketball under arena lights">
    <span class="label"><em>Recreation</em>Basketball<svg width="18" height="22" viewBox="0 0 18 22"><path d="M4 2 L14 11 L4 20" fill="none" stroke="#1d4f86" stroke-width="4"/></svg></span>
  </a>
  <a class="tile tile--rs" href="http://krvlathletics-example.com/soccer/index.html" role="img" aria-label="Photo of a soccer ball on a grass field">
    <span class="label"><em>Recreation</em>Soccer<svg width="18" height="22" viewBox="0 0 18 22"><path d="M4 2 L14 11 L4 20" fill="none" stroke="#1d4f86" stroke-width="4"/></svg></span>
  </a>
  <a class="tile tile--cb" href="http://www.krvlherons-example.com/" role="img" aria-label="Photo of youth players in a basketball game">
    <span class="label"><em>Competitive</em>Basketball<svg width="18" height="22" viewBox="0 0 18 22"><path d="M4 2 L14 11 L4 20" fill="none" stroke="#1d4f86" stroke-width="4"/></svg></span>
  </a>
  <a class="tile tile--cs" href="http://www.ridgepremiersoccer-example.com/" role="img" aria-label="Photo of youth players in a soccer match">
    <span class="label"><em>Competitive</em>Soccer<svg width="18" height="22" viewBox="0 0 18 22"><path d="M4 2 L14 11 L4 20" fill="none" stroke="#1d4f86" stroke-width="4"/></svg></span>
  </a>
</main>

<nav class="footer-nav">
  <a href="#">ABOUT US</a> / <a href="#">CONTACT US</a><span>/</span><a href="#">JOIN KRVL EMAIL LIST</a> /<span></span><a href="#">OUR VISION</a><span>/</span><a href="#">OUR OFFICE</a>
</nav>
</body>
</html>
```